Powerpoint Slides for 'Lantern Ridge | consulting' firm

Hello,

I would like a suite of slides to not be typical of just ANOther deck. My business name is 'Lantern Ridge | consulting', so I would like to see innovation and creativity translated into the slides.

1. ‘Company/Cover Page’ – should showcase Lantern Ridge | consulting branding; perhaps with some animation to give the sense of 'out of the box' content.
The company name, Lantern Ridge | consulting, and tagline - Strategise | Organise | Optimise | Communicate, should appear together on the front and end page. The company name should appear on all other pages
2. Master branded background slide, with suggested font, and ideally with some colour options which could be leveraged in longer presentations to ‘break’ it up
3. Master branded background slide with an option to include bulleted content within some type of e.g. shape/form (not just as bullets against a blank background)
4. Divider slide (possibly leveraging some of the colours in Point 2

I have attached a copy of the logo/layout of my business card. The square used is raised on the business card which gives a very subtle effect of literally being out of the box. I would like something of a similar feel, but with colour (as noted in Point 2), though very open to ideas/suggestions.

Many Thanks,
Marisol
Updates

This project has been re-opened to all designers. I look forward to seeing creative and innovative submissions. Best Regards, Marisol

Target Market(s)

SMEs and Corporates - however, I don't want to look like just any other consultancy company.

Industry/Entity Type

Business

Colors

Designer to choose colors to be used in the design.

Requirements
Must have
• Innovation; Creativity; Professionalism; Succinct

```html
<!DOCTYPE html>
<html lang="en">
<head>
<meta charset="utf-8">
<title>Lantern Ridge | consulting – slide suite</title>
<link rel="stylesheet" href="https://fonts.googleapis.com/css2?family=Questrial&family=Open+Sans:wght@400;700&display=swap">
<style>
:root{
  --canvas:#b9cbe0;
  --label:#2c3e55;
  --star:#5a7cae;
  --white:#ffffff;
  --grey-light:#d9d9d9;
  --grey-dark:#3b3b3b;
  --ink:#2f2f2f;
  --muted:#5a6470;
  --green:#1db14b;
  --olive:#6f8f2a;
  --navy:#1e4a86;
  --teal:#39a7c6;
}
*{box-sizing:border-box;margin:0;padding:0}
html,body{width:1200px;height:456px;overflow:hidden;background:var(--canvas)}
body{font-family:"Questrial",sans-serif;color:var(--ink)}
.sorter{display:grid;grid-template-columns:repeat(5,229px);column-gap:10.5px;padding:6px 0 0 6px}
.cell{height:150px}
.slide{position:relative;width:229px;height:136px;background:var(--white);overflow:hidden;box-shadow:0 0 0 1px rgba(0,0,0,.12)}
.label{display:flex;justify-content:space-between;align-items:center;height:14px;padding:0 2px;font-family:"Open Sans",sans-serif;font-size:8px;color:var(--label)}
.label svg{width:8px;height:8px}

.brand-tag{position:absolute;left:96px;top:118px;width:38px;height:12px;background:#e4e4e4;font-size:3px;color:#888;display:flex;align-items:center;justify-content:center;line-height:1}

/* section divider */
.section{background:var(--grey-light)}
.section.fade{background:linear-gradient(160deg,#dcdcdc 0%,#bdbdbd 55%,#8e8e8e 100%)}
.section .band{position:absolute;left:0;right:0;top:57px;height:27px;background:var(--grey-dark)}
.section .frame{position:absolute;left:13px;top:47px;width:40px;height:47px;border:5px solid var(--accent)}
.section .title{position:absolute;left:27px;top:58px;font-size:18px;line-height:24px;color:var(--white);white-space:nowrap}
.section .subtitle{position:absolute;left:60px;top:86px;font-size:11px;color:var(--ink);white-space:nowrap}

/* title bar slides */
.topbar{position:absolute;left:0;right:0;top:0;height:14px;background:var(--grey-dark)}
.topbar .mark{position:absolute;left:8px;top:1px;width:14px;height:14px;border:2px solid var(--accent)}
.topbar h2{position:absolute;left:24px;top:1px;font-family:"Open Sans",sans-serif;font-weight:700;font-size:9px;line-height:12px;color:var(--white)}
.topbar .num{position:absolute;right:6px;top:2px;width:10px;height:9px;background:#8a8a8a;font-size:3px;color:#fff;text-align:center;line-height:9px}
.bullets{position:absolute;list-style:none;font-family:"Open Sans",sans-serif;font-size:5px;line-height:6.5px;color:#444}
.bullets li{position:relative;padding-left:8px;margin-bottom:6px}
.bullets li::before{content:"";position:absolute;left:1px;top:2.3px;width:2px;height:2px;border-radius:50%;background:#444}
.question{position:absolute;left:14px;top:23px;width:201px;height:14px;background:#d8d8d8;font-family:"Open Sans",sans-serif;font-weight:700;font-size:7.5px;line-height:14px;padding-left:10px}
.side-panel{position:absolute;left:14px;top:37px;width:26px;height:76px;background:#e8e8e8}
.side-panel.fade{background:linear-gradient(180deg,#eeeeee,#9c9c9c)}

/* cover */
.cover .wordmark{position:absolute;left:0;right:0;top:40px;text-align:center;font-size:10px;letter-spacing:2px;color:var(--muted);white-space:nowrap}
.cover .tagline{position:absolute;left:0;right:0;top:72px;text-align:center;font-size:3.4px;letter-spacing:.6px;color:var(--muted)}
.cover .footer{position:absolute;left:0;right:0;top:112px;bottom:0;background:#dcdcdc}
.cover .presented{position:absolute;left:146px;top:118px;font-size:5px;color:#777;padding-right:6px;border-right:1px solid #999}

/* team */
.team{position:absolute;top:22px;width:50px}
.team .photo{position:relative;width:40px;height:36px;margin-left:6px;margin-top:5px}
.team .photo::before{content:"";position:absolute;left:-6px;top:-5px;width:30px;height:30px;border-top:4px solid #bdbdbd;border-left:4px solid #bdbdbd}
.team .photo span{position:absolute;inset:0;background:#efefef;border:1px solid #e0e0e0}
.team h3{font-family:"Open Sans",sans-serif;font-size:4px;font-weight:700;margin-top:5px;color:var(--ink)}
.team .role{font-size:2.8px;font-weight:700;color:#555;margin-top:1px}
.team p{font-family:"Open Sans",sans-serif;font-size:2.8px;line-height:3.4px;color:#555;padding-left:3px;margin-top:1px}

/* promise slide */
.promise-photo{position:absolute;left:0;top:14px;width:104px;height:122px;background:linear-gradient(135deg,#8a8a8a,#3a3a3a 60%,#1e1e1e)}
.promise-box{position:absolute;left:4px;top:90px;width:56px;height:40px;background:var(--navy);color:var(--white);font-family:"Open Sans",sans-serif;font-weight:700;font-size:5px;line-height:6px;padding:6px 5px}
.promise-copy{position:absolute;left:112px;top:22px;width:110px;font-family:"Open Sans",sans-serif}
.promise-copy h3{font-family:"Questrial",sans-serif;font-size:8.5px;font-weight:400;color:var(--ink);margin-bottom:3px}
.promise-copy p{font-size:3.3px;line-height:4px;color:#444;margin-bottom:3px}

/* feature slides */
.features-band{position:absolute;left:0;right:0;top:22px;height:36px;background:linear-gradient(90deg,#f2f2f2,#8f8f8f 50%,#f2f2f2)}
.feature{position:absolute;top:30px;width:52px}
.feature .icon{width:20px;height:18px;margin-left:8px;background:var(--white);border:1px solid #ddd;display:flex;align-items:center;justify-content:center}
.feature .icon svg{width:12px;height:12px}
.feature h3{font-family:"Open Sans",sans-serif;font-weight:700;font-size:4.6px;margin-top:8px;color:var(--ink)}
.feature p{font-family:"Open Sans",sans-serif;font-size:3.2px;line-height:3.9px;color:#555;margin-top:2px}
</style>
</head>
<body>
<main class="sorter">

  <div class="cell">
    <section class="slide cover">
      <div class="wordmark">LANTERN RIDGE | CONSULTING</div>
      <div class="tagline">Strategise | Organise | Optimise | Communicate</div>
      <div class="footer"></div>
      <div class="presented">Presented by</div>
    </section>
    <div class="label"><svg viewBox="0 0 10 10"><path d="M5 .8l1.2 2.7 2.9.3-2.2 2 .7 2.9L5 7.2 2.4 8.7l.7-2.9-2.2-2 2.9-.3z" fill="none" stroke="var(--star)" stroke-width=".8"/></svg><span>1</span></div>
  </div>

  <div class="cell">
    <section class="slide section" style="--accent:var(--green)">
      <div class="band"></div><div class="frame"></div>
      <div class="title">Section Title</div><div class="subtitle">Subtitle heading</div>
      <div class="brand-tag">Lantern Ridge</div>
    </section>
    <div class="label"><svg viewBox="0 0 10 10"><path d="M5 .8l1.2 2.7 2.9.3-2.2 2 .7 2.9L5 7.2 2.4 8.7l.7-2.9-2.2-2 2.9-.3z" fill="none" stroke="var(--star)" stroke-width=".8"/></svg><span>2</span></div>
  </div>

  <div class="cell">
    <section class="slide section fade" style="--accent:var(--green)">
      <div class="band"></div><div class="frame"></div>
      <div class="title">Section Title</div><div class="subtitle">Subtitle heading</div>
      <div class="brand-tag">Lantern Ridge</div>
    </section>
    <div class="label"><svg viewBox="0 0 10 10"><path d="M5 .8l1.2 2.7 2.9.3-2.2 2 .7 2.9L5 7.2 2.4 8.7l.7-2.9-2.2-2 2.9-.3z" fill="none" stroke="var(--star)" stroke-width=".8"/></svg><span>3</span></div>
  </div>

  <div class="cell">
    <section class="slide" style="--accent:var(--green)">
      <header class="topbar"><span class="mark"></span><h2>MEET OUR TEAM</h2><span class="num">4</span></header>
      <div class="team" style="left:16px"><div class="photo" role="img" aria-label="Team member portrait"><span></span></div><h3>Tessa Quill</h3><div class="role">Lead Consultant</div><p>Consectetuer adipiscing elit. Maecenas porttitor congue massa. Fusce posuere, magna sed pulvinar ultricies.</p></div>
      <div class="team" style="left:85px"><div class="photo" role="img" aria-label="Team member portrait"><span></span></div><h3>Nora Vale</h3><div class="role">Lead Consultant</div><p>Consectetuer adipiscing elit. Maecenas porttitor congue massa. Fusce posuere, magna sed pulvinar ultricies.</p></div>
      <div class="team" style="left:154px"><div class="photo" role="img" aria-label="Team member portrait"><span></span></div><h3>Owen Pryce</h3><div class="role">Lead Consultant</div><p>Consectetuer adipiscing elit. Maecenas porttitor congue massa. Fusce posuere, magna sed pulvinar ultricies.</p></div>
      <div class="brand-tag">Lantern Ridge</div>
    </section>
    <div class="label"><svg viewBox="0 0 10 10"><path d="M5 .8l1.2 2.7 2.9.3-2.2 2 .7 2.9L5 7.2 2.4 8.7l.7-2.9-2.2-2 2.9-.3z" fill="none" stroke="var(--star)" stroke-width=".8"/></svg><span>4</span></div>
  </div>

  <div class="cell">
    <section class="slide" style="--accent:var(--green)">
      <header class="topbar"><span class="mark"></span><h2>TITLE SLIDE</h2><span class="num">5</span></header>
      <ul class="bullets" style="left:12px;top:22px;width:200px">
        <li>Consectetuer adipiscing elit. Vivamus a tellus.</li>
        <li>Nunc viverra imperdiet enim. Fusce est.</li>
        <li>Maecenas porttitor congue massa.</li>
        <li>Fusce posuere, magna sed pulvinar ultricies, purus lectus malesuada libero, sit amet commodo magna eros quis?</li>
      </ul>
      <div class="brand-tag">Lantern Ridge</div>
    </section>
    <div class="label"><svg viewBox="0 0 10 10"><path d="M5 .8l1.2 2.7 2.9.3-2.2 2 .7 2.9L5 7.2 2.4 8.7l.7-2.9-2.2-2 2.9-.3z" fill="none" stroke="var(--star)" stroke-width=".8"/></svg><span>5</span></div>
  </div>

  <div class="cell">
    <section class="slide section" style="--accent:var(--olive)">
      <div class="band"></div><div class="frame"></div>
      <div class="title">Section Title</div><div class="subtitle">Subtitle heading</div>
      <div class="brand-tag">Lantern Ridge</div>
    </section>
    <div class="label"><svg viewBox="0 0 10 10"><path d="M5 .8l1.2 2.7 2.9.3-2.2 2 .7 2.9L5 7.2 2.4 8.7l.7-2.9-2.2-2 2.9-.3z" fill="none" stroke="var(--star)" stroke-width=".8"/></svg><span>6</span></div>
  </div>

  <div class="cell">
    <section class="slide" style="--accent:var(--olive)">
      <header class="topbar"><span class="mark"></span><h2>TITLE SLIDE</h2><span class="num">7</span></header>
      <div class="question">Lorem ipsum dolor?</div>
      <div class="side-panel"></div>
      <ul class="bullets" style="left:54px;top:44px;width:160px">
        <li>Consectetuer adipiscing elit. Vivamus a tellus.</li>
        <li>Nunc viverra imperdiet enim. Fusce est.</li>
        <li>Maecenas porttitor congue massa.</li>
        <li>Fusce posuere, magna sed pulvinar ultricies, purus lectus malesuada libero, sit amet commodo magna eros quis?</li>
      </ul>
      <div class="brand-tag">Lantern Ridge</div>
    </section>
    <div class="label"><svg viewBox="0 0 10 10"><path d="M5 .8l1.2 2.7 2.9.3-2.2 2 .7 2.9L5 7.2 2.4 8.7l.7-2.9-2.2-2 2.9-.3z" fill="none" stroke="var(--star)" stroke-width=".8"/></svg><span>7</span></div>
  </div>

  <div class="cell">
    <section class="slide" style="--accent:var(--olive)">
      <header class="topbar"><span class="mark"></span><h2>TITLE SLIDE</h2><span class="num">8</span></header>
      <div class="question">Lorem ipsum dolor?</div>
      <div class="side-panel fade" style="left:0;width:40px;height:99px"></div>
      <ul class="bullets" style="left:54px;top:44px;width:160px">
        <li>Consectetuer adipiscing elit. Vivamus a tellus.</li>
        <li>Nunc viverra imperdiet enim. Fusce est.</li>
        <li>Maecenas porttitor congue massa.</li>
        <li>Fusce posuere, magna sed pulvinar ultricies, purus lectus malesuada libero, sit amet commodo magna eros quis?</li>
      </ul>
      <div class="brand-tag">Lantern Ridge</div>
    </section>
    <div class="label"><svg viewBox="0 0 10 10"><path d="M5 .8l1.2 2.7 2.9.3-2.2 2 .7 2.9L5 7.2 2.4 8.7l.7-2.9-2.2-2 2.9-.3z" fill="none" stroke="var(--star)" stroke-width=".8"/></svg><span>8</span></div>
  </div>

  <div class="cell">
    <section class="slide" style="--accent:var(--olive)">
      <header class="topbar"><span class="mark"></span><h2>TITLE SLIDE</h2><span class="num">9</span></header>
      <ul class="bullets" style="left:12px;top:22px;width:200px">
        <li>Consectetuer adipiscing elit. Vivamus a tellus.</li>
        <li>Nunc viverra imperdiet enim. Fusce est.</li>
        <li>Maecenas porttitor congue massa.</li>
        <li>Fusce posuere, magna sed pulvinar ultricies, purus lectus malesuada libero, sit amet commodo magna eros quis?</li>
      </ul>
      <div class="brand-tag">Lantern Ridge</div>
    </section>
    <div class="label"><svg viewBox="0 0 10 10"><path d="M5 .8l1.2 2.7 2.9.3-2.2 2 .7 2.9L5 7.2 2.4 8.7l.7-2.9-2.2-2 2.9-.3z" fill="none" stroke="var(--star)" stroke-width=".8"/></svg><span>9</span></div>
  </div>

  <div class="cell">
    <section class="slide section" style="--accent:var(--navy)">
      <div class="band"></div><div class="frame"></div>
      <div class="title">Section Title</div><div class="subtitle">Subtitle heading</div>
      <div class="brand-tag">Lantern Ridge</div>
    </section>
    <div class="label"><svg viewBox="0 0 10 10"><path d="M5 .8l1.2 2.7 2.9.3-2.2 2 .7 2.9L5 7.2 2.4 8.7l.7-2.9-2.2-2 2.9-.3z" fill="none" stroke="var(--star)" stroke-width=".8"/></svg><span>10</span></div>
  </div>

  <div class="cell">
    <section class="slide" style="--accent:var(--navy)">
      <div class="promise-photo" role="img" aria-label="Photo of a hand sketching lightbulb ideas, dark grey tones"></div>
      <header class="topbar"><span class="mark"></span><h2>TITLE SLIDE</h2><span class="num">11</span></header>
      <div class="promise-box">Our promise to you and your business</div>
      <div class="promise-copy">
        <h3>We're here to look after you.</h3>
        <p>Consectetuer adipiscing elit. Maecenas porttitor congue massa. Fusce posuere, magna sed pulvinar ultricies, purus lectus malesuada libero, sit amet commodo magna eros quis urna.</p>
        <p>Nunc viverra imperdiet enim. Fusce est. Vivamus a tellus.</p>
        <p>Pellentesque habitant morbi tristique senectus et netus et malesuada fames ac turpis egestas. Proin pharetra nonummy pede. Mauris et orci.</p>
      </div>
      <div class="brand-tag" style="left:112px">Lantern Ridge</div>
    </section>
    <div class="label"><svg viewBox="0 0 10 10"><path d="M5 .8l1.2 2.7 2.9.3-2.2 2 .7 2.9L5 7.2 2.4 8.7l.7-2.9-2.2-2 2.9-.3z" fill="none" stroke="var(--star)" stroke-width=".8"/></svg><span>11</span></div>
  </div>

  <div class="cell">
    <section class="slide" style="--accent:var(--navy)">
      <header class="topbar"><span class="mark"></span><h2>TITLE SLIDE</h2><span class="num">12</span></header>
      <ul class="bullets" style="left:12px;top:22px;width:200px">
        <li>Consectetuer adipiscing elit. Vivamus a tellus.</li>
        <li>Nunc viverra imperdiet enim. Fusce est.</li>
        <li>Maecenas porttitor congue massa.</li>
        <li>Fusce posuere, magna sed pulvinar ultricies, purus lectus malesuada libero, sit amet commodo magna eros quis?</li>
      </ul>
      <div class="brand-tag">Lantern Ridge</div>
    </section>
    <div class="label"><svg viewBox="0 0 10 10"><path d="M5 .8l1.2 2.7 2.9.3-2.2 2 .7 2.9L5 7.2 2.4 8.7l.7-2.9-2.2-2 2.9-.3z" fill="none" stroke="var(--star)" stroke-width=".8"/></svg><span>12</span></div>
  </div>

  <div class="cell">
    <section class="slide section" style="--accent:var(--teal)">
      <div class="band"></div><div class="frame"></div>
      <div class="title">Section Title</div><div class="subtitle">Subtitle heading</div>
      <div class="brand-tag">Lantern Ridge</div>
    </section>
    <div class="label"><svg viewBox="0 0 10 10"><path d="M5 .8l1.2 2.7 2.9.3-2.2 2 .7 2.9L5 7.2 2.4 8.7l.7-2.9-2.2-2 2.9-.3z" fill="none" stroke="var(--star)" stroke-width=".8"/></svg><span>13</span></div>
  </div>

  <div class="cell">
    <section class="slide" style="--accent:var(--teal)">
      <header class="topbar"><span class="mark"></span><h2>TITLE SLIDE</h2><span class="num">14</span></header>
      <div class="feature" style="left:14px"><div class="icon"><svg viewBox="0 0 12 12"><path d="M6 1.5a3.2 3.2 0 0 0-2 5.7V8.5h4V7.2a3.2 3.2 0 0 0-2-5.7z" fill="none" stroke="var(--teal)" stroke-width=".9"/><path d="M4.5 9.8h3" stroke="var(--teal)" stroke-width=".9"/></svg></div><h3>Lorem ipsum dolor</h3><p>Consectetuer adipiscing elit. Maecenas porttitor congue massa. Fusce posuere, magna sed pulvinar ultricies, purus lectus malesuada libero, sit amet commodo magna eros quis?</p></div>
      <div class="feature" style="left:88px"><div class="icon"><svg viewBox="0 0 12 12"><path d="M2 10.5h8M3 10.5V4.5h6v6M4 4.5V2.5h4v2" fill="none" stroke="var(--teal)" stroke-width=".9"/></svg></div><h3>Lorem ipsum dolor</h3><p>Consectetuer adipiscing elit. Maecenas porttitor congue massa. Fusce posuere, magna sed pulvinar ultricies, purus lectus malesuada libero, sit amet commodo magna eros quis?</p></div>
      <div class="feature" style="left:162px"><div class="icon"><svg viewBox="0 0 12 12"><path d="M1.5 10.5h9" stroke="var(--teal)" stroke-width=".9"/><rect x="2.5" y="7" width="1.6" height="3.5" fill="var(--teal)"/><rect x="5.2" y="5" width="1.6" height="5.5" fill="var(--teal)"/><rect x="7.9" y="3" width="1.6" height="7.5" fill="var(--teal)"/></svg></div><h3>Lorem ipsum dolor</h3><p>Consectetuer adipiscing elit. Maecenas porttitor congue massa. Fusce posuere, magna sed pulvinar ultricies, purus lectus malesuada libero, sit amet commodo magna eros quis?</p></div>
      <div class="brand-tag">Lantern Ridge</div>
    </section>
    <div class="label"><svg viewBox="0 0 10 10"><path d="M5 .8l1.2 2.7 2.9.3-2.2 2 .7 2.9L5 7.2 2.4 8.7l.7-2.9-2.2-2 2.9-.3z" fill="none" stroke="var(--star)" stroke-width=".8"/></svg><span>14</span></div>
  </div>

  <div class="cell">
    <section class="slide" style="--accent:var(--teal)">
      <header class="topbar"><span class="mark"></span><h2>TITLE SLIDE</h2><span class="num">15</span></header>
      <div class="features-band"></div>
      <div class="feature" style="left:14px"><div class="icon"><svg viewBox="0 0 12 12"><path d="M6 1.5a3.2 3.2 0 0 0-2 5.7V8.5h4V7.2a3.2 3.2 0 0 0-2-5.7z" fill="none" stroke="var(--teal)" stroke-width=".9"/><path d="M4.5 9.8h3" stroke="var(--teal)" stroke-width=".9"/></svg></div><h3>Lorem ipsum dolor</h3><p>Consectetuer adipiscing elit. Maecenas porttitor congue massa. Fusce posuere, magna sed pulvinar ultricies, purus lectus malesuada libero, sit amet commodo magna eros quis?</p></div>
      <div class="feature" style="left:88px"><div class="icon"><svg viewBox="0 0 12 12"><path d="M2 10.5h8M3 10.5V4.5h6v6M4 4.5V2.5h4v2" fill="none" stroke="var(--teal)" stroke-width=".9"/></svg></div><h3>Lorem ipsum dolor</h3><p>Consectetuer adipiscing elit. Maecenas porttitor congue massa. Fusce posuere, magna sed pulvinar ultricies, purus lectus malesuada libero, sit amet commodo magna eros quis?</p></div>
      <div class="feature" style="left:162px"><div class="icon"><svg viewBox="0 0 12 12"><path d="M1.5 10.5h9" stroke="var(--teal)" stroke-width=".9"/><rect x="2.5" y="7" width="1.6" height="3.5" fill="var(--teal)"/><rect x="5.2" y="5" width="1.6" height="5.5" fill="var(--teal)"/><rect x="7.9" y="3" width="1.6" height="7.5" fill="var(--teal)"/></svg></div><h3>Lorem ipsum dolor</h3><p>Consectetuer adipiscing elit. Maecenas porttitor congue massa. Fusce posuere, magna sed pulvinar ultricies, purus lectus malesuada libero, sit amet commodo magna eros quis?</p></div>
      <div class="brand-tag">Lantern Ridge</div>
    </section>
    <div class="label"><svg viewBox="0 0 10 10"><path d="M5 .8l1.2 2.7 2.9.3-2.2 2 .7 2.9L5 7.2 2.4 8.7l.7-2.9-2.2-2 2.9-.3z" fill="none" stroke="var(--star)" stroke-width=".8"/></svg><span>15</span></div>
  </div>

</main>
</body>
</html>
```